Business card design needed

We are starting an online scrapbooking store (craft), home based in Brisbane, Australia
We would like the 'Steampunk' look on our card using steampunk colour palette
Sunny Paper Nook
Online Scrapbooking Store
specialising in DIY kits
find inspiration at
www.sunnypapernook.com.au
email: sunnypapernook@quillmailbox.com

Hi There,

Sorry people, but I was informed last night, from one designer that they hadn't received the picture I said I had uploaded :(
I have again, attempted to upload it, hope it turns up so you can see what we have created to start with.

Thank you so much :)
Tess

Industry/Entity Type

Store

Contact Information for Business Card

Sunny Paper Nook
Online Scrapbooking Store specialising in DIY kits
find inspiration at www.sunnypapernook.com.au

Requirements
Must have
• We have provided/uploaded a picture of what we have created so far - Steampunk girl, cogs, flowers etc If you google 'steampunk color palette' you will have an idea of the colours we would like to utilize. Also if you google 'brindle-47-38592' it will give you an idea of the style of steampunk flowers and colours we would like to use

```html
<!DOCTYPE html>
<html lang="en">
<head>
<meta charset="utf-8">
<title>Sunny Paper Nook – Business Card</title>
<link href="https://fonts.googleapis.com/css2?family=Delius&display=swap" rel="stylesheet">
<style>
  :root {
    --backdrop: #2a3236;
    --card-brown: #8b6b4f;
    --stripe-dark: #7c5e44;
    --panel-brown: #8a6a4e;
    --wood-light: #a8845c;
    --wood-dark: #654a31;
    --ink: #3a2216;
    --ink-soft: #4a2c1e;
    --gold: #c9a24a;
    --screw: #b9b5a6;
    --screw-edge: #6f6a5c;
    --button: #d8cfc4;
  }
  * { box-sizing: border-box; margin: 0; padding: 0; }
  html, body { width: 1200px; height: 741px; overflow: hidden; }
  body {
    background: var(--backdrop);
    position: relative;
    font-family: "Delius", "Comic Sans MS", sans-serif;
    color: var(--ink);
  }
  .card {
    position: absolute;
    left: 320px;
    width: 560px;
    height: 320px;
    overflow: hidden;
    box-shadow: 0 4px 14px rgba(0,0,0,0.5);
  }
  .card-front { top: 40px; background: var(--card-brown); }
  .card-back { top: 381px; }

  /* front */
  .front-stripes {
    position: absolute; inset: 0;
    background: repeating-linear-gradient(90deg, var(--card-brown) 0 14px, var(--stripe-dark) 14px 28px);
    opacity: 0.55;
  }
  .front-wood-edge {
    position: absolute; left: 0; top: 0; bottom: 0; width: 34px;
    background: linear-gradient(90deg, var(--wood-dark), var(--wood-light));
  }
  .front-artwork {
    position: absolute; left: 22px; top: 16px; width: 232px; height: 290px;
    background: linear-gradient(160deg, #b39473 0%, #8e6f52 45%, #b78a78 100%);
    border-radius: 6px;
  }
  .gold-thread {
    position: absolute; left: 20px; right: 0; top: 16px; height: 2px;
    background: var(--gold);
  }
  .front-text {
    position: absolute; left: 256px; right: 10px; top: 0; bottom: 0;
    text-align: center;
  }
  .brand-name {
    position: absolute; left: 0; right: 0; top: 54px;
    font-size: 21px; letter-spacing: 2px; text-transform: uppercase;
  }
  .tagline {
    position: absolute; left: 0; right: 0; top: 90px;
    font-size: 15px; font-style: italic; line-height: 31px; color: var(--ink-soft);
  }
  .inspiration-label {
    position: absolute; left: 0; right: 0; top: 180px;
    font-size: 16px; font-style: italic; text-decoration: underline;
  }
  .website {
    position: absolute; left: 0; right: 0; top: 207px;
    font-size: 13px; font-style: italic;
  }
  .email {
    position: absolute; left: 0; right: 0; top: 283px;
    font-size: 12px; font-style: italic;
  }

  .screw, .button-dot {
    position: absolute; border-radius: 50%;
  }
  .screw {
    width: 20px; height: 20px;
    background: var(--screw); border: 2px solid var(--screw-edge);
  }
  .button-dot {
    width: 11px; height: 11px;
    background: var(--button); border: 1px solid var(--screw-edge);
  }

  /* back */
  .back-shape { position: absolute; inset: 0; }
  .back-text { position: absolute; inset: 0; text-align: center; }
  .back-name {
    position: absolute; left: 0; right: 0; top: 118px;
    font-size: 23px; letter-spacing: 2px; text-transform: uppercase;
  }
  .back-website {
    position: absolute; left: 0; right: 0; top: 152px;
    font-size: 13px; font-style: italic;
  }
  .back-tagline {
    position: absolute; left: 0; right: 0; top: 240px;
    font-size: 16px; font-style: italic; color: var(--ink-soft);
  }
</style>
</head>
<body>

<section class="card card-front" aria-label="Business card front">
  <div class="front-stripes"></div>
  <div class="front-wood-edge"></div>
  <div class="front-artwork" role="img" aria-label="Scrapbook frame with paper flowers, buttons, bows and a little girl in a pink dress"></div>
  <div class="gold-thread"></div>
  <span class="screw" style="left:6px; top:6px;"></span>
  <span class="button-dot" style="left:238px; top:12px;"></span>
  <span class="button-dot" style="left:520px; top:134px;"></span>
  <span class="button-dot" style="left:238px; top:292px;"></span>

  <div class="front-text">
    <h1 class="brand-name">Sunny Paper Nook</h1>
    <p class="tagline">Online Scrapbooking Store<br>specialising in DIY KITS</p>
    <p class="inspiration-label">Find inspiration at</p>
    <p class="website">www.sunnypapernook.com.au</p>
    <p class="email">email: sunnypapernook@quillmailbox.com</p>
  </div>
</section>

<section class="card card-back" aria-label="Business card back">
  <svg class="back-shape" width="560" height="320" viewBox="0 0 560 320">
    <defs>
      <linearGradient id="woodGrain" x1="0" y1="0" x2="1" y2="0">
        <stop offset="0" stop-color="#654a31"/>
        <stop offset="0.5" stop-color="#a8845c"/>
        <stop offset="1" stop-color="#654a31"/>
      </linearGradient>
    </defs>
    <rect width="560" height="320" fill="url(#woodGrain)"/>
    <path d="M40 0 H520 C510 25 520 45 545 50 C560 80 560 100 540 110
             C515 125 515 150 540 165 V265
             C520 270 505 275 490 295 C475 312 455 300 430 300
             H330 C310 300 300 320 280 320 C260 320 250 300 230 300
             H130 C105 300 85 312 70 295 C55 275 40 270 20 265
             V165 C45 150 45 125 20 110 C0 100 0 80 15 50
             C40 45 50 25 40 0 Z"
          fill="var(--panel-brown)" stroke="#c9b49a" stroke-width="1.5"/>
    <circle cx="20" cy="300" r="10" fill="var(--screw)" stroke="var(--screw-edge)" stroke-width="2"/>
    <circle cx="540" cy="300" r="10" fill="var(--screw)" stroke="var(--screw-edge)" stroke-width="2"/>
  </svg>
  <div class="back-text">
    <h2 class="back-name">Sunny Paper Nook</h2>
    <p class="back-website">www.sunnypapernook.com.au</p>
    <p class="back-tagline">Online Scrapbooking Store</p>
  </div>
</section>

</body>
</html>
```